HRC

This is to hand out to folks at conferences to tell them about this list serve and direct them to the site to email in to join it.
This is a networking and resource site for mental health and addiction professionals.
The mission statement on the ABOUT page needs to be on it.
Then the website address and my name Marta Quillon, LICSW
List Serve Moderator and my email Marta@MartaQuillon.net
and my phone 202-555-0148.
Please see website: www.harborreferralcircle.net

Industry/Entity Type

Mental Health

Contact Information for Business Card

Front: name Harbor Referral Circle and mission statement on the "About" page and put website address: www.harborreferralcircle.net and my name Marta Quillon, LICSW ListServ Moderator
Back: info on the list serve with instructions to go to Contact Us page.
Anything you all think might be useful and still look good.
Put my cell # on the back, 202-555-0193

```html
<!DOCTYPE html>
<html lang="en">
<head>
<meta charset="utf-8">
<title>Harbor Referral Circle – Business Cards</title>
<link href="https://fonts.googleapis.com/css2?family=Libre+Baskerville:wght@400;700&family=Crimson+Text:wght@400;600&display=swap" rel="stylesheet">
<style>
  :root {
    --bg: #d9d9d9;
    --red: #b8262f;
    --red-light: #d8333c;
    --blue: #1f5b80;
    --blue-dark: #174766;
    --peach: #d99a82;
    --peach-light: #e8b9a4;
    --accent-faint: #c94a45;
    --white: #ffffff;
    --cream: #fbeee4;
  }
  * { box-sizing: border-box; margin: 0; padding: 0; }
  html, body { width: 1200px; height: 900px; overflow: hidden; }
  body {
    background: var(--bg);
    position: relative;
    font-family: "Crimson Text", Georgia, serif;
  }
  .card {
    position: absolute;
    width: 700px;
    height: 400px;
    overflow: hidden;
    background: linear-gradient(160deg, var(--red) 0%, var(--red) 55%, var(--red-light) 100%);
    box-shadow: 0 6px 18px rgba(0,0,0,.25);
  }
  .card--front { left: 140px; top: 30px; }
  .card--back  { left: 360px; top: 470px; }

  .band-top {
    position: absolute; left: 0; top: 0; width: 100%; height: 22px;
    background: var(--blue);
  }
  .band-top__accent {
    position: absolute; right: 14px; top: 6px; width: 118px; height: 10px;
    background: linear-gradient(90deg, rgba(255,255,255,.55), rgba(255,255,255,.85));
  }

  .accent-area {
    position: absolute; left: 0; top: 85px; width: 110px; height: 200px;
    background: linear-gradient(90deg, var(--accent-faint) 0%, rgba(201,74,69,0) 100%);
    opacity: .8;
  }

  .title {
    position: absolute; left: 0; top: 30px; width: 100%; text-align: center;
    font-family: "Libre Baskerville", Georgia, serif;
    font-weight: 700; color: var(--white);
    font-size: 33px; letter-spacing: .3px;
  }

  .body-text {
    position: absolute; top: 80px; left: 90px; right: 70px;
    color: var(--cream); text-align: center;
    font-size: 17px; line-height: 21px;
  }
  .card--back .body-text { left: 70px; right: 60px; }

  .band-peach {
    position: absolute; left: 0; top: 292px; width: 100%; height: 48px;
    background: linear-gradient(90deg, var(--peach) 0%, var(--peach-light) 100%);
  }

  .band-bottom {
    position: absolute; left: 0; bottom: 0; width: 100%; height: 60px;
    background: var(--blue);
    border-top: 4px solid var(--blue-dark);
  }

  .name {
    position: absolute; left: 24px; top: 290px;
    font-family: "Libre Baskerville", Georgia, serif;
    font-weight: 700; font-size: 38px; color: var(--white);
    white-space: nowrap;
  }

  .contact-block {
    position: absolute; right: 24px; top: 294px;
    text-align: right; color: var(--white);
    font-family: "Libre Baskerville", Georgia, serif;
  }
  .role { font-size: 17px; line-height: 22px; }
  .email { font-size: 14px; line-height: 20px; }

  .phone {
    position: absolute; right: 24px; top: 296px;
    display: flex; align-items: center; gap: 8px;
    font-family: "Libre Baskerville", Georgia, serif;
    font-weight: 700; font-size: 32px; color: var(--white);
    white-space: nowrap;
  }
  .phone svg { width: 26px; height: 30px; fill: var(--white); }

  .website {
    position: absolute; left: 0; bottom: 12px; width: 100%;
    text-align: center;
    font-family: "Libre Baskerville", Georgia, serif;
    font-weight: 700; font-size: 28px; color: var(--cream);
    letter-spacing: .5px;
  }
</style>
</head>
<body>

<section class="card card--front">
  <div class="band-top">
    <div class="band-top__accent" role="img" aria-label="Row of small decorative stars"></div>
  </div>
  <div class="accent-area" role="img" aria-label="Large faint decorative star"></div>
  <h1 class="title">Harbor Referral Circle</h1>
  <p class="body-text">The Harbor Referral Circle Listserv began on December 10, 2010 with a few names of professionals that wanted to keep connection with each other. Today the listserv has over 400 members and is growing strong. This listserv include addiction and mental health professionals of all kinds from around the country and even one internationally that share resources, help each other find the right placements for their patients/clients, toss around important issues, invite each other to valuable events and much more.</p>
  <div class="band-peach"></div>
  <div class="name">Marta Quillon</div>
  <div class="contact-block">
    <div class="role">LICSW ListServ Moderator</div>
    <div class="email">Marta@MartaQuillon.net</div>
  </div>
  <div class="band-bottom"><div class="website">www.harborreferralcircle.net</div></div>
</section>

<section class="card card--back">
  <div class="band-top">
    <div class="band-top__accent" role="img" aria-label="Row of small decorative stars"></div>
  </div>
  <div class="accent-area" role="img" aria-label="Large faint decorative star"></div>
  <h2 class="title">Harbor Referral Circle</h2>
  <p class="body-text">Joining the Listserv is easy, go to the “Contact Us” tab, fill in the form and let us know that you’d like to become a member. You will then be sent an invitation to join the Group from Tidewell Groups. Next, follow the prompts to “Join this Mailing List”, there will be two prompts for that. You do not need to Join the Group, only JOIN THIS MAILING LIST. Once you do that you will receive an email welcoming you to the listserv and telling you how to use this wonderful resource.</p>
  <div class="band-peach"></div>
  <div class="name">Marta Quillon</div>
  <div class="phone">
    <svg viewBox="0 0 24 28"><path d="M7 2c1 0 2 .6 2.3 1.6l1.3 4c.3 1-.1 2-1 2.5l-1.5.9c.8 3 2.6 6 5 8l1.4-1c.9-.6 2-.5 2.7.3l2.7 3c.7.8.7 2-.1 2.8l-1.6 1.6C16.5 27 13 26 10 22.5 6.5 18.5 3.5 12 4.5 6.3 4.8 4 5.5 2 7 2z"/></svg>
    <span>202-555-0193</span>
  </div>
  <div class="band-bottom"><div class="website">www.harborreferralcircle.net</div></div>
</section>

</body>
</html>
```